Webdesign für ambulanter Pflegedienst
Zielgruppe
Es ist ein ambulanter Pflegedienst, der sich im Raum Dessau-Roßlau um die Versorgung sowie Betreuung von Menschen kümmert. Kontaktdaten: ambulanter Pflegedienst Hand Sorge; Inhaberin: Sabine Lohmar; Birkenweg 14, 06871 Dessau-Roßlau Telefon: 034907/519364
IK-Nummer: 47 283 6194
e-mail: sl-hand-sorge@postfeld.de
Aufgabenstellung
Die Farben sollen in Anlehnung an das Logo sein, dass mit übersandt wird.

```html
<!DOCTYPE html>
<html lang="de">
<head>
<meta charset="utf-8">
<title>Unsere Leistungen – Hand Sorge</title>
<link href="https://fonts.googleapis.com/css2?family=Raleway:wght@400;500;600;700&family=Shadows+Into+Light+Two&display=swap" rel="stylesheet">
<style>
:root{
  --teal:#45a9a6;
  --teal-dark:#3a9996;
  --green:#62ad35;
  --sky:#dcedf8;
  --text:#5c5c5c;
  --text-soft:#6e6e6e;
  --line:#d9d9d9;
  --white:#ffffff;
  --hero-a:#add9d6;
  --hero-b:#e7efe9;
}
*{box-sizing:border-box;margin:0;padding:0}
html,body{width:1200px;height:2346px;overflow:hidden;background:var(--white)}
body{font-family:"Raleway",sans-serif;color:var(--text);position:relative}
.script{font-family:"Shadows Into Light Two",cursive}

/* header */
.site-header{position:absolute;left:0;top:0;width:1200px;height:50px;background:var(--white)}
.brand{position:absolute;left:264px;top:15px;display:flex;align-items:center;gap:6px;font-size:11px;font-weight:600;color:var(--text)}
.brand-dot{width:12px;height:12px;border-radius:50%;background:var(--teal)}
.main-nav{position:absolute;left:418px;top:17px;display:flex;gap:0;font-size:13px}
.main-nav a{text-decoration:none;color:var(--text-soft);margin-right:31px}
.main-nav a.active{color:var(--green);font-weight:600}
.tagline{position:absolute;left:0;top:50px;width:1200px;height:26px;background:var(--sky);text-align:center;font-size:11px;line-height:26px;color:var(--text)}
.tagline b{color:var(--teal);font-weight:500}

/* hero */
.hero{position:absolute;left:0;top:76px;width:1200px;height:181px;background:linear-gradient(90deg,var(--hero-a) 0%,var(--hero-b) 55%,#e7ebe6 62%)}
.hero-photo{position:absolute;left:660px;top:0;width:540px;height:181px;background:linear-gradient(90deg,rgba(231,235,230,0) 0%,#d7b9a3 25%,#c99a7e 55%,#b98a70 80%,#d9cbc0 100%)}
.hero-kicker{position:absolute;left:263px;top:52px;font-size:17px;color:var(--text)}
.hero-title{position:absolute;left:263px;top:80px;font-size:31px;font-weight:700;color:var(--text)}
.hero-badge{position:absolute;left:716px;top:163px;width:142px;height:142px;border-radius:50%;background:var(--white);box-shadow:0 4px 12px rgba(0,0,0,.12);display:flex;align-items:center;justify-content:center}

/* accordion */
.services{position:absolute;left:263px;top:360px;width:674px}
.panel{background:var(--white);border-radius:6px;box-shadow:0 1px 5px rgba(0,0,0,.16);margin-bottom:6px}
.panel-head{height:58px;display:flex;align-items:center;justify-content:space-between;padding:0 22px 0 30px}
.panel-head h2{font-size:19px;font-weight:700;color:var(--text)}
.toggle{width:16px;height:16px;position:relative}
.toggle::before,.toggle::after{content:"";position:absolute;background:var(--teal)}
.toggle::before{left:0;top:6px;width:16px;height:4px}
.toggle.plus::after{left:6px;top:0;width:4px;height:16px}
.panel-body{padding:6px 30px 32px 30px;font-size:12.2px;line-height:15.6px;color:var(--text-soft)}
.fristen{width:608px;margin:22px 0 30px 3px;border:1px solid #9a9a9a;border-top:none;border-collapse:collapse;font-size:12.2px}
.fristen th{background:var(--sky);text-align:left;font-weight:700;color:var(--text);padding:12px 12px 8px;height:52px;vertical-align:top;line-height:15.6px}
.fristen td{padding:3px 12px;height:28px;vertical-align:top;line-height:15px}
.fristen tr.first td{padding-top:24px;height:112px}
.fristen tr.last td{padding-bottom:12px}

/* contact form */
.contact{position:absolute;left:330px;top:1430px;width:524px;height:498px;background:var(--white);border-radius:6px;box-shadow:0 1px 8px rgba(0,0,0,.15);overflow:hidden}
.contact-head{height:56px;background:var(--sky);text-align:center;line-height:56px;font-size:17px;color:var(--text)}
.field{position:absolute}
.field label{display:block;font-size:12.5px;color:var(--text);margin-bottom:7px}
.field .box{border:1px solid #c9c9c9;border-radius:8px;height:40px}
.consent{position:absolute;left:39px;top:365px;display:flex;gap:17px;font-size:9.6px;line-height:13.6px;color:var(--text-soft);width:450px}
.consent .check{flex:none;width:28px;height:28px;border:1px solid #c9c9c9;border-radius:5px}
.consent a{color:var(--teal);text-decoration:none}
.send{position:absolute;left:346px;top:430px;width:153px;height:45px;border-radius:23px;background:var(--teal);color:var(--white);font-size:12px;font-weight:700;display:flex;align-items:center;justify-content:center;box-shadow:0 3px 6px rgba(0,0,0,.18)}

/* footer */
.site-footer{position:absolute;left:0;top:2062px;width:1200px;height:235px;background:linear-gradient(90deg,var(--hero-a) 0%,var(--hero-b) 50%)}
.footer-photo{position:absolute;left:640px;top:0;width:560px;height:235px;background:linear-gradient(90deg,rgba(231,239,233,0) 0%,#d8b59a 25%,#b98258 55%,#a8714b 80%,#c79a75 100%)}
.footer-info{position:absolute;left:261px;top:26px;font-size:12.7px;line-height:19px;color:var(--text)}
.footer-info h3{font-weight:400;font-size:19px;margin-bottom:12px}
.footer-info p+p{margin-top:12px}
.footer-brand{position:absolute;left:520px;top:104px;width:160px;text-align:center;display:flex;flex-direction:column;align-items:center;gap:8px;font-size:17px;font-weight:500;color:var(--text)}
.footer-brand span.mark{width:44px;height:44px;border-radius:50%;border:3px solid var(--teal)}
.to-top{position:absolute;left:832px;top:2004px;width:104px;height:104px;border-radius:50%;background:var(--sky);display:flex;flex-direction:column;align-items:center;justify-content:center;gap:6px;font-size:14px;color:var(--text);z-index:2}
.bottom-bar{position:absolute;left:0;top:2297px;width:1200px;height:49px;background:var(--sky);font-size:10px}
.bottom-bar nav a{position:absolute;top:20px;font-weight:700;color:var(--text);text-decoration:none}
.copyright{position:absolute;left:707px;top:20px;font-size:8.5px;color:var(--text-soft)}
</style>
</head>
<body>

<header class="site-header">
  <div class="brand"><span class="brand-dot"></span>Hand Sorge</div>
  <nav class="main-nav">
    <a href="#">Startseite</a>
    <a href="#">Sofortige Hilfen</a>
    <a href="#" class="active">Unsere Leistungen</a>
    <a href="#">Karriere</a>
    <a href="#">Pflegekurse</a>
  </nav>
</header>
<div class="tagline"><b>Hand Sorge</b> - <span class="script">Pflege von Mensch zu Mensch</span></div>

<section class="hero">
  <div class="hero-photo" role="img" aria-label="Foto: viele übereinandergelegte Hände als Zeichen des Zusammenhalts"></div>
  <p class="hero-kicker script">vollumfänglicher Service für Sie</p>
  <h1 class="hero-title">Unsere Leistungen</h1>
</section>
<div class="hero-badge">
  <svg width="60" height="54" viewBox="0 0 60 54" aria-hidden="true">
    <path d="M30 50 C10 36 4 26 4 16 A12 12 0 0 1 30 12 A12 12 0 0 1 56 16 C56 26 50 36 30 50Z" fill="#5c5c5c"/>
  </svg>
</div>

<main class="services">
  <section class="panel"><div class="panel-head"><h2>Grundpflege</h2><span class="toggle plus"></span></div></section>
  <section class="panel"><div class="panel-head"><h2>Behandlungspflege</h2><span class="toggle plus"></span></div></section>
  <section class="panel">
    <div class="panel-head"><h2>Beratungseinsatz nach §37 Abs. 3 SGB XI</h2><span class="toggle"></span></div>
    <div class="panel-body">
      <p>Für Pflegegeldempfänger ist der Beratungseinsatz nach §37 Abs. 3 SGB XI verpflichtend. Dies bedeutet, dass Pflegebedürftige, die Pflegegeld für die häusliche Pflege beziehen und dabei keinerlei Hilfe von einer professionellen Pflegekraft erhalten, gesetzlich dazu verpflichtet sind, sich regelmäßig beraten zu lassen. Jeder Pflegegeldempfänger kann dabei selbstständig entscheiden von wem er sich beraten lässt. Es kann sowohl eine von der Pflegekasse beauftragte Pflegefachkraft sein als auch ein zugelassener Pflegedienst. Nachstehend sind folgende Fristen für die Beratung gesetzlich verankert und aufgezeigt.</p>
      <table class="fristen">
        <thead><tr><th style="width:193px">Pflegegeldempfänger<br>je Pflegegrad</th><th style="width:178px">Beratungseinsatz nach<br>§37 Abs. 3 SGB XI</th><th>Einzuhaltende Fristen<br>der Beratung</th></tr></thead>
        <tbody>
          <tr class="first"><td>Pflegegrad 1</td><td style="padding-top:26px">Nicht zwangsläufig vorgschrieben, 1 x pro Halbjahr möglich</td><td style="padding-top:26px">keine</td></tr>
          <tr><td>Pflegegrad 2</td><td>1 x pro Halbjahr</td><td>30.06., 31.12.</td></tr>
          <tr><td>Pflegegrad 3</td><td>1x pro Halbjahr</td><td>30.06., 31.12.</td></tr>
          <tr><td>Pflegegrad 4</td><td>1 x pro Vierteljahr</td><td>31.03., 30.06., 30.09., 31.12.</td></tr>
          <tr class="last"><td>Pflegegrad 5</td><td>1 x por Vierteljahr</td><td>31.03., 30.06., 30.09., 31.12.</td></tr>
        </tbody>
      </table>
      <p>Selbstverständlich übernehmen wir diese Beratung gern für sie. Dabei ist es unser Ziel sie über das Angebot der Pflegekasse sowie der Krankenkassen aufzuklären. Dies beinhaltet die Durchführung von Pflegekursen beziehungsweise Einzelschulungen (gem. § 45 SGB XI) oder weitere Entlastungsmöglichkeiten für pflegende Angehörige.</p>
    </div>
  </section>
  <section class="panel"><div class="panel-head"><h2>Verhinderungspflege nach §39 SGB XII</h2><span class="toggle plus"></span></div></section>
  <section class="panel"><div class="panel-head"><h2>Entlastungs- und Betreuungsangebote gem. §45b SGB XI</h2><span class="toggle plus"></span></div></section>
  <section class="panel"><div class="panel-head"><h2>Hauswirtschaftliche Leistungen</h2><span class="toggle plus"></span></div></section>
  <section class="panel"><div class="panel-head"><h2>Sonstige Leistungen</h2><span class="toggle plus"></span></div></section>
</main>

<form class="contact">
  <div class="contact-head script">Nehmen Sie Kontakt mit uns auf!</div>
  <div class="field" style="left:39px;top:86px;width:223px"><label>Nachname*</label><div class="box"></div></div>
  <div class="field" style="left:276px;top:86px;width:223px"><label>Vorname*</label><div class="box"></div></div>
  <div class="field" style="left:39px;top:163px;width:256px"><label>E-Mail*</label><div class="box"></div></div>
  <div class="field" style="left:309px;top:163px;width:190px"><label>Telefonnummer*</label><div class="box"></div></div>
  <div class="field" style="left:39px;top:239px;width:460px"><label>Ihr Anliegen:</label><div class="box" style="height:86px"></div></div>
  <div class="consent"><span class="check"></span><p>Sie erklären sich damit einverstanden, dass Ihre Daten zur Bearbeitung Ihres Anliegens verwendet werden. Weitere Informationen und Widerrufshinweise finden Sie in der <a href="#">Datenschutzerklärung</a>.</p></div>
  <div class="send">Abenden</div>
</form>

<a class="to-top" href="#">
  <svg width="20" height="32" viewBox="0 0 20 32" aria-hidden="true"><path d="M10 0 L20 16 H12.5 V32 H7.5 V16 H0Z" fill="#45a9a6"/></svg>
  <span class="script">Nach oben</span>
</a>

<footer class="site-footer">
  <div class="footer-photo" role="img" aria-label="Foto: Hände vieler Menschen im Kreis auf einem Holztisch"></div>
  <div class="footer-info">
    <h3 class="script">Wir sind für Sie da!</h3>
    <p>ambulanter Pflegedienst Hand Sorge<br>Inhaberin: Sabine Lohmar<br>Birkenweg 14<br>06871 Dessau-Roßlau</p>
    <p>034907/519364<br>sl-hand-sorge@postfeld.de</p>
  </div>
  <div class="footer-brand"><span class="mark"></span>HAND SORGE</div>
</footer>

<div class="bottom-bar">
  <nav>
    <a href="#" style="left:274px">KARRIERE</a>
    <a href="#" style="left:369px">KONTAKT</a>
    <a href="#" style="left:470px">DATENSCHUTZ</a>
    <a href="#" style="left:596px">IMPRESSUM</a>
  </nav>
  <p class="copyright">Copyright 2023 © ambulanter Pflegedienst Hand Sorge</p>
</div>

</body>
</html>
```